Used Car Business Card Design

Maple Ridge Auto Sales is a woman owned women friendly car lot.  We focus on providing Professionalism, Integrity and Respect beginning with the initial introduction.  We place the highest importance on customer service after the sale and our rating with the TVB of Arkansas shows it.  We're starting out 7th year, recently relocated. Satisfied Clients bring their family members, friends and co-workers to buy their cars, SUV's and trucks from MRAS.
You buy here / you pay here, Lending program opportunities too, Great Cash Prices
Finance with Flexibility we look at each individual uniquely and not a credit score
I think of my kids when getting our vehicles ready and your safety when you drive away in a MRAS car. . .  Drive away with Peace of Mind...
Maroon, Black and Silver colors.

Updates
I sent a response to the designers - have  not heard from them, will I receive my funds back?

Thank you all,  a lot of great designs - Making my decision on Nov 4th

So much talent. . .
So very challenging. . .
Thank you for your participation.
Sincerely,
Maple Ridge Auto Sales
Lorna Pickett

Industry/Entity Type
Safety
Contact Information for Business Card
Maple Ridge Auto Sales
"A Sound Car at a Fair Price"
4153 Garvey Rd. North Little Rock, Ar 72118
Lorna Pickett
501.389.7312

```html
<!DOCTYPE html>
<html lang="en">
<head>
<meta charset="utf-8">
<title>Maple Ridge Auto Sales – Business Card</title>
<link rel="stylesheet" href="https://fonts.googleapis.com/css2?family=Raleway:wght@700&family=Arimo:wght@400&display=swap">
<style>
  :root {
    --backdrop: #efe8de;
    --card: #ffffff;
    --maroon: #6b0a0a;
    --ink: #0a0a0a;
    --silver: #c4c4c4;
  }
  html, body {
    margin: 0;
    padding: 0;
    width: 1200px;
    height: 1200px;
    overflow: hidden;
    background: var(--backdrop);
  }
  .business-card {
    position: absolute;
    left: 48px;
    top: 273px;
    width: 1085px;
    height: 634px;
    background: var(--card);
    text-align: center;
  }
  .company-name {
    position: absolute;
    left: 0; right: 0;
    top: 100px;
    margin: 0;
    font-family: "Raleway", sans-serif;
    font-weight: 700;
    font-size: 50px;
    line-height: 1;
    color: var(--maroon);
  }
  .tagline {
    position: absolute;
    left: 0; right: 0;
    top: 198px;
    margin: 0;
    font-family: "Arimo", sans-serif;
    font-weight: 400;
    font-size: 36px;
    line-height: 1;
    color: var(--ink);
  }
  .person-name {
    position: absolute;
    left: 0; right: 0;
    top: 303px;
    margin: 0;
    font-family: "Raleway", sans-serif;
    font-weight: 700;
    font-size: 62px;
    line-height: 1;
    color: var(--ink);
  }
  .phone {
    position: absolute;
    left: 0; right: 0;
    top: 385px;
    margin: 0;
    font-family: "Arimo", sans-serif;
    font-size: 31px;
    letter-spacing: 1px;
    line-height: 1;
    color: var(--ink);
  }
  .address-band {
    position: absolute;
    left: 0; right: 0; bottom: 0;
    height: 130px;
    background: var(--maroon);
    display: flex;
    align-items: flex-start;
    justify-content: center;
  }
  .address {
    margin: 40px 0 0;
    font-family: "Arimo", sans-serif;
    font-size: 33px;
    letter-spacing: 0.5px;
    line-height: 1;
    color: var(--silver);
  }
</style>
</head>
<body>
  <section class="business-card">
    <h1 class="company-name">Maple Ridge Auto Sales</h1>
    <p class="tagline">"A Sound Car at a Fair Price"</p>
    <h2 class="person-name">Lorna Pickett</h2>
    <p class="phone">501.389.7312</p>
    <footer class="address-band">
      <p class="address">4153 Garvey Rd. North Little Rock, Ar 72118</p>
    </footer>
  </section>
</body>
</html>
```